Corporate A4 Advert for Worldwide Timber Trader/Agent

We need a new professional company ad, which will be used in worldwide magazine publications. something sophisticated.
Our website - www.qrolumber.co.uk - for info. We are timber agents and sell timber from one part of the world to another.
I will upload a selection of product photos to include - suggest using not all but a selection of some them, to showcase the product. Our buyers purchase both logs and sawn timber
We would like this ad to list our source areas and product groups.
Our company colour is British Racing Green
Updates

Target Market(s)

timber buyers

Industry/Entity Type

Timber

Colors
00AB8E
00BBA5
67D7C9
C6EFE9
E9F9F6

Requirements
Must have
• company logo

```html
<!DOCTYPE html>
<html lang="en">
<head>
<meta charset="utf-8">
<title>QRO International Timber Agents – Advert</title>
<link rel="stylesheet" href="https://fonts.googleapis.com/css2?family=Montserrat:wght@400;500;600;700&display=swap">
<style>
  :root {
    --backdrop: #626262;
    --racing-green: #262f25;
    --lime: #b5d334;
    --paper: #f5f7f7;
    --ink: #262b26;
    --white: #ffffff;
    --timber-light: #c9773f;
    --timber-dark: #8a4a26;
    --forest: #4a5d45;
  }
  * { box-sizing: border-box; margin: 0; padding: 0; }
  html, body {
    width: 907px; height: 1200px; overflow: hidden;
    background: var(--backdrop);
    font-family: "Montserrat", Arial, sans-serif;
  }
  .advert {
    position: absolute; left: 65px; top: 50px;
    width: 777px; height: 1098px;
    background: var(--paper);
    box-shadow: 8px 8px 8px rgba(0,0,0,0.45);
    overflow: hidden;
  }
  .hero-band {
    position: absolute; left: 0; top: 0; width: 100%; height: 440px;
    background: var(--racing-green);
  }
  .brand {
    position: absolute; left: 0; top: 0; width: 268px; text-align: center; color: var(--white);
  }
  .brand-mark {
    position: absolute; left: 74px; top: 70px;
    width: 120px; height: 120px; border-radius: 50%;
    background: var(--white);
  }
  .brand-name {
    position: absolute; left: 0; top: 222px; width: 100%;
    font-size: 54px; font-weight: 700; letter-spacing: 1px; line-height: 1;
  }
  .brand-tagline {
    position: absolute; left: 0; top: 288px; width: 100%;
    font-size: 20px; font-weight: 500; line-height: 27px; letter-spacing: 0.5px;
  }
  .headline {
    position: absolute; left: 280px; top: 66px;
    color: var(--white); font-size: 34px; font-weight: 400; line-height: 45px; letter-spacing: 0.5px;
  }
  .headline strong { color: var(--lime); font-weight: 700; }
  .source-areas {
    position: absolute; left: 280px; top: 186px; list-style: none;
    color: var(--white); font-size: 24px; font-weight: 400; letter-spacing: 0.5px;
  }
  .source-areas li { height: 46px; line-height: 30px; }
  .source-areas li::before {
    content: ""; display: inline-block; width: 6px; height: 6px; border-radius: 50%;
    background: var(--lime); margin: 0 6px 5px 2px; vertical-align: middle;
  }
  .product-photo {
    position: absolute; left: 0; top: 400px; width: 100%; height: 430px;
    background:
      linear-gradient(to bottom, var(--racing-green) 0%, rgba(38,47,37,0) 18%, rgba(245,247,247,0) 82%, var(--paper) 100%),
      linear-gradient(to bottom, var(--forest) 0%, var(--forest) 30%, var(--timber-dark) 45%, var(--timber-light) 70%, #b86a3d 100%);
  }
  .product-groups {
    position: absolute; left: 0; top: 820px; width: 100%;
    display: flex; justify-content: center; align-items: center; gap: 34px;
    color: var(--ink); font-size: 46px; font-weight: 500; letter-spacing: 1px; line-height: 1;
  }
  .product-groups .divider { width: 3px; height: 58px; background: var(--ink); }
  .contact-prompt {
    position: absolute; left: 0; top: 900px; width: 100%; text-align: center;
    color: var(--ink); font-size: 24px; font-weight: 400; line-height: 33px; letter-spacing: 0.3px;
  }
  .contact-prompt strong { font-weight: 700; }
  .phone {
    position: absolute; left: 0; top: 976px; width: 100%;
    display: flex; justify-content: center; align-items: center; gap: 6px;
    color: var(--ink); font-size: 28px; font-weight: 700;
  }
  .footer-wave { position: absolute; left: 0; bottom: 0; width: 777px; height: 66px; }
  .footer-links {
    position: absolute; left: 0; bottom: 12px; width: 100%;
    display: flex; justify-content: center; align-items: center; gap: 16px;
    color: var(--white); font-size: 21px; font-weight: 500;
  }
  .footer-links span { display: flex; align-items: center; gap: 6px; }
</style>
</head>
<body>
  <main class="advert">
    <section class="hero-band">
      <div class="brand">
        <div class="brand-mark"></div>
        <div class="brand-name">QRO</div>
        <div class="brand-tagline">INTERNATIONAL<br>TIMBER AGENTS</div>
      </div>
      <h1 class="headline">QUALITY <strong>TIMBER</strong><br>DELIVERED WORLDWIDE</h1>
      <ul class="source-areas">
        <li>AFRICA</li>
        <li>EUROPE</li>
        <li>NORTH &amp; SOUTH AMERICA</li>
        <li>ASIA</li>
      </ul>
    </section>

    <div class="product-photo" role="img" aria-label="Photo of stacked hardwood logs beside strapped packs of sawn timber in a forest timber yard"></div>

    <div class="product-groups">
      <span>LOGS</span><span class="divider"></span><span>SAWN TIMBER</span>
    </div>

    <p class="contact-prompt">CONTACT OUR <strong>EXPERT TEAM</strong> TO HELP<br>FULFIL YOUR TIMBER REQUIREMENTS</p>

    <div class="phone">
      <svg width="34" height="34" viewBox="0 0 24 24" aria-hidden="true">
        <path fill="#b5d334" d="M6.6 10.8c1.4 2.8 3.8 5.1 6.6 6.6l2.2-2.2c.3-.3.7-.4 1-.2 1.1.4 2.3.6 3.6.6.6 0 1 .4 1 1V20c0 .6-.4 1-1 1C10.6 21 3 13.4 3 4c0-.6.4-1 1-1h3.5c.6 0 1 .4 1 1 0 1.3.2 2.5.6 3.6.1.3 0 .7-.2 1L6.6 10.8z"/>
      </svg>
      <span>+44(0)20 7946 0321</span>
    </div>

    <svg class="footer-wave" viewBox="0 0 777 66" preserveAspectRatio="none" aria-hidden="true">
      <path fill="#262f25" d="M0 66 C60 62 80 4 170 2 L600 2 C690 4 720 60 777 66 Z"/>
    </svg>
    <div class="footer-links">
      <span>
        <svg width="22" height="22" viewBox="0 0 24 24" aria-hidden="true" fill="none" stroke="#b5d334" stroke-width="2">
          <circle cx="12" cy="12" r="10"/><ellipse cx="12" cy="12" rx="4.5" ry="10"/><path d="M2 12h20M4 7h16M4 17h16"/>
        </svg>
        www.qrolumber.co.uk
      </span>
      <span>
        <svg width="24" height="18" viewBox="0 0 24 18" aria-hidden="true">
          <rect x="0" y="0" width="24" height="18" rx="2" fill="#b5d334"/>
          <path d="M1 2l11 8 11-8" fill="none" stroke="#262f25" stroke-width="2"/>
        </svg>
        sales@qrolumber.co.uk
      </span>
    </div>
  </main>
</body>
</html>
```